Oil and gas industry project solutions company needs professional cards with Canadian aboriginal fee

We are a aboriginally owned company that is focused on Project Planning, Management, Inspection & Consulting for Canada's Petroleum Industry. We have a logo that we would like to incorporate into a professional looking business card. We are professionals that offer services from project inception to completion.

Target Market(s)

Major industry leaders like NorthRidge Pipelines, Vantor, Kelstrand Energy, Brimwell etc.

Industry/Entity Type

Industry

Contact Information for Business Card

Reid Forbin
reid@kolbymarsh.ca
250 418 9067

Requirements
Must have
• KolbyMarsh Inc. logo.
• Address is: RR4, Site2, Comp7 Fort St. John, BC V1J 8K3 Traditional Territory of the Treaty 8 People
• Colors that are in logo
• Banner or picture on back
• Ability to put different names and contacts
• Website: kolbymarsh.ca
• "Project Planning, Management, Inspection & Consulting for Canada's Petroleum Industry"

```html
<!DOCTYPE html>
<html lang="en">
<head>
<meta charset="utf-8">
<title>KolbyMarsh Inc. Business Card</title>
<link rel="stylesheet" href="https://fonts.googleapis.com/css2?family=Open+Sans:wght@400;700&family=Playfair+Display:wght@400&display=swap">
<style>
  :root {
    --navy: #232a6e;
    --green: #5aa539;
    --ink: #222222;
    --rule: #555555;
    --paper: #f7f7f7;
    --stage: #e6e3de;
    --photo-sky: #c9d3dc;
    --photo-mid: #7f93a6;
    --photo-dark: #3b4656;
  }
  * { margin: 0; padding: 0; box-sizing: border-box; }
  html, body { width: 1200px; height: 902px; overflow: hidden; }
  body {
    background: var(--stage);
    font-family: "Open Sans", sans-serif;
    display: flex;
    flex-direction: column;
    align-items: center;
    justify-content: center;
    gap: 36px;
  }
  .card {
    position: relative;
    width: 700px;
    height: 400px;
    background: var(--paper);
    overflow: hidden;
    box-shadow: 0 4px 14px rgba(0,0,0,0.18);
  }

  /* Back side */
  .back-photo {
    position: absolute; inset: 0;
    background: linear-gradient(160deg, var(--photo-dark) 0%, var(--photo-mid) 35%, var(--photo-sky) 60%, var(--photo-mid) 80%, var(--photo-dark) 100%);
  }
  .back-band {
    position: absolute; left: 0; right: 0; top: 130px; height: 130px;
    background: rgba(255,255,255,0.72);
    display: flex; align-items: center; justify-content: center;
  }

  /* Wordmark */
  .wordmark { display: flex; align-items: center; gap: 14px; }
  .wordmark-dot { width: 26px; height: 26px; border-radius: 50%; background: var(--green); flex: none; }
  .wordmark-name {
    font-weight: 700; font-size: 44px; line-height: 1; color: var(--navy); letter-spacing: -0.5px;
  }

  /* Front side */
  .swoosh { position: absolute; inset: 0; }
  .front-brand { position: absolute; left: 60px; top: 56px; }
  .front-brand .wordmark-dot { width: 60px; height: 60px; }
  .front-brand .wordmark-name { font-size: 46px; }
  .brand-rule {
    position: absolute; left: 150px; top: 146px; width: 500px; height: 1px;
    background: var(--rule);
  }
  .divider {
    position: absolute; left: 405px; top: 168px; width: 1px; height: 96px;
    background: var(--ink);
  }
  .contacts {
    position: absolute; left: 430px; top: 166px; list-style: none;
    font-size: 17px; color: var(--ink); line-height: 29px;
  }
  .contacts li { display: flex; align-items: center; gap: 12px; }
  .contacts svg { width: 16px; height: 16px; flex: none; }
  .person-name {
    position: absolute; left: 60px; top: 232px;
    font-family: "Playfair Display", serif; font-size: 38px; line-height: 1.2; color: var(--navy);
  }
  .address-text { font-size: 15px; fill: #ffffff; }
</style>
</head>
<body>

  <section class="card card-front" aria-label="Business card front">
    <svg class="swoosh" viewBox="0 0 700 400" width="700" height="400" aria-hidden="true">
      <path d="M0 400 L0 396 C 200 350, 470 318, 700 298 L700 400 Z" fill="var(--green)"/>
      <path d="M30 392 C 240 320, 470 290, 700 270 L700 286 C 470 306, 240 336, 30 392 Z" fill="var(--navy)"/>
      <path id="address-path" d="M170 393 C 340 352, 500 332, 690 316" fill="none"/>
      <text class="address-text"><textPath href="#address-path">RR4, Site2, Comp7 Fort St. John, BC V1J 8K3</textPath></text>
    </svg>

    <div class="front-brand wordmark">
      <span class="wordmark-dot"></span>
      <span class="wordmark-name">KolbyMarsh Inc.</span>
    </div>
    <div class="brand-rule"></div>
    <div class="divider"></div>

    <ul class="contacts">
      <li>
        <svg viewBox="0 0 16 16"><rect width="16" height="16" fill="var(--navy)"/><path d="M5 3.5 L7 6 L6 7 C6.6 8.4 7.6 9.4 9 10 L10 9 L12.5 11 L11.5 12.5 C7.5 12.3 3.8 8.5 3.5 4.5 Z" fill="#fff"/></svg>
        250 418 9067
      </li>
      <li>
        <svg viewBox="0 0 16 16"><rect width="16" height="16" fill="var(--navy)"/><circle cx="8" cy="8" r="4.5" fill="none" stroke="#fff" stroke-width="1.2"/><path d="M3.5 8 H12.5 M8 3.5 V12.5" stroke="#fff" stroke-width="1"/></svg>
        www.kolbymarsh.ca
      </li>
      <li>
        <svg viewBox="0 0 16 16"><rect width="16" height="16" fill="var(--navy)"/><rect x="3.5" y="5" width="9" height="6.5" fill="none" stroke="#fff" stroke-width="1.1"/><path d="M3.5 5 L8 8.8 L12.5 5" fill="none" stroke="#fff" stroke-width="1.1"/></svg>
        reid@kolbymarsh.ca
      </li>
    </ul>

    <p class="person-name">Reid Forbin</p>
  </section>

  <section class="card card-back" aria-label="Business card back">
    <div class="back-photo" role="img" aria-label="Photo of pipeline construction in a snowy field with crews in safety gear"></div>
    <div class="back-band">
      <div class="wordmark">
        <span class="wordmark-dot"></span>
        <span class="wordmark-name">KolbyMarsh Inc.</span>
      </div>
    </div>
  </section>

</body>
</html>
```